M Zyvantics Buisness Cards

I need a technology focused clean business card for my employees. I have attached out logo to include in the mocks. We're a modern tech consulting firm that drives to interface humanity with technology in a truly cohesive fashion.

```html
<!DOCTYPE html>
<html lang="en">
<head>
<meta charset="utf-8">
<title>M Zyvantics Business Cards</title>
<link href="https://fonts.googleapis.com/css2?family=Nunito+Sans:wght@400;600;700&display=swap" rel="stylesheet">
<style>
  :root {
    --stage: #3e4148;
    --card: #f6f6f7;
    --ink-grey: #6d6e71;
    --rule-grey: #8a8b8e;
    --brand-blue: #1a78c8;
    --band-blue-light: #35aee6;
    --band-blue-dark: #0a7fcf;
    --band-dark: #2e3034;
    --accent-grey: #8e9096;
    --white: #ffffff;
  }
  * { box-sizing: border-box; margin: 0; padding: 0; }
  html, body { width: 811px; height: 1200px; overflow: hidden; }
  body {
    background: var(--stage);
    font-family: "Nunito Sans", Arial, sans-serif;
    position: relative;
  }
  .card {
    position: absolute;
    width: 414px;
    height: 237px;
    background: var(--card);
    overflow: hidden;
  }
  .card-back { left: 72px; top: 355px; }
  .card-front { left: 293px; top: 607px; }

  .brand {
    position: absolute;
    display: flex;
    align-items: center;
    color: var(--ink-grey);
    font-weight: 700;
    white-space: nowrap;
  }
  .brand-dot {
    border-radius: 50%;
    background: var(--brand-blue);
    flex: none;
  }
  .card-back .brand { left: 0; right: 0; top: 0; bottom: 0; justify-content: center; font-size: 36px; gap: 12px; }
  .card-back .brand-dot { width: 26px; height: 26px; }
  .card-front .brand { left: 26px; top: 56px; font-size: 19px; gap: 7px; }
  .card-front .brand-dot { width: 14px; height: 14px; }

  .divider {
    position: absolute;
    left: 192px; top: 32px;
    width: 2px; height: 92px;
    background: var(--rule-grey);
  }
  .identity { position: absolute; left: 226px; top: 30px; color: var(--ink-grey); }
  .identity .name { font-size: 16px; font-weight: 600; line-height: 1.2; }
  .identity .role { font-size: 10.5px; font-weight: 600; margin-top: 1px; }

  .contacts { position: absolute; left: 226px; top: 74px; list-style: none; }
  .contacts li {
    display: flex; align-items: center; gap: 7px;
    height: 19px;
    font-size: 11px; color: var(--ink-grey); letter-spacing: 0.2px;
  }
  .contacts svg { width: 14px; height: 14px; flex: none; }

  .bands { position: absolute; left: 0; top: 0; width: 414px; height: 237px; }
</style>
</head>
<body>

  <section class="card card-back" aria-label="Business card back">
    <div class="brand"><span class="brand-dot"></span>M Zyvantics</div>
  </section>

  <section class="card card-front" aria-label="Business card front">
    <div class="brand"><span class="brand-dot"></span>M Zyvantics</div>
    <div class="divider"></div>

    <div class="identity">
      <p class="name">Employee Name</p>
      <p class="role">Designation</p>
    </div>

    <ul class="contacts">
      <li>
        <svg viewBox="0 0 14 14"><circle cx="7" cy="7" r="7" fill="var(--brand-blue)"/><rect x="4.6" y="3" width="4.8" height="8" rx="1" fill="none" stroke="#fff" stroke-width="1.1"/></svg>
        123-456-789
      </li>
      <li>
        <svg viewBox="0 0 14 14"><circle cx="7" cy="7" r="7" fill="var(--brand-blue)"/><rect x="3.5" y="4.5" width="7" height="5" fill="#fff"/><path d="M3.5 4.5 L7 7.3 L10.5 4.5" fill="none" stroke="var(--brand-blue)" stroke-width="0.9"/></svg>
        loremipsum@info.com
      </li>
      <li>
        <svg viewBox="0 0 14 14"><circle cx="7" cy="7" r="7" fill="var(--brand-blue)"/><g fill="none" stroke="#fff" stroke-width="0.8"><circle cx="7" cy="7" r="3.8"/><ellipse cx="7" cy="7" rx="1.6" ry="3.8"/><line x1="3.2" y1="7" x2="10.8" y2="7"/></g></svg>
        www.loremipsum.com
      </li>
    </ul>

    <svg class="bands" viewBox="0 0 414 237" aria-hidden="false">
      <defs>
        <linearGradient id="blueBand" x1="0" y1="0" x2="1" y2="1">
          <stop offset="0" stop-color="var(--band-blue-light)"/>
          <stop offset="1" stop-color="var(--band-blue-dark)"/>
        </linearGradient>
      </defs>
      <rect class="band-dark" x="250" y="170" width="164" height="67" fill="var(--band-dark)" role="img" aria-label="Dark band with fine geometric pattern"/>
      <polygon class="band-blue" points="0,142 240,142 276,237 0,237" fill="url(#blueBand)" role="img" aria-label="Blue band with network constellation artwork"/>
      <polygon points="255,186 255,221 286,203" fill="none" stroke="var(--accent-grey)" stroke-width="2" opacity="0.8"/>
      <polygon points="290,174 290,190 304,182" fill="none" stroke="var(--accent-grey)" stroke-width="1.5" opacity="0.6"/>
      <polygon points="294,216 294,236 312,226" fill="var(--accent-grey)"/>
    </svg>
  </section>

</body>
</html>
```